E-mail newsletter design - brightloomer

We are a gaming app developer

When an in-app game finishes, we would like to mail people taking part in leagues with a table showing where they finished along with all other players.

There could be up to 20 players in each league.

The mail shows the name of the league they are in and has an announcement regarding the game currently going on.

The mail should be HTML formatted and follow the look and feel of our website

Mail should be branded based on which app is sending the mail
brightloom goalpost - see brightloomgoalpost.example
brightloom scrum - see brightloomscrum.example
brightloom quizpot see brightloomquizpot.example

It should include a graphic element that is able to be written over, containing the placeholder text "Don't forget to play (name of next game) starting on (date)"

Requirements
Must have
• Any graphical elements should be provided separately

```html
<!DOCTYPE html>
<html lang="en">
<head>
<meta charset="utf-8">
<title>brightloom goalpost – League Standings</title>
<link rel="stylesheet" href="https://fonts.googleapis.com/css2?family=Questrial&family=Open+Sans:wght@700;800&display=swap">
<style>
  :root {
    --sky: #b0e1fb;
    --sky-glow: #ffffff;
    --panel: #f3f3f3;
    --panel-edge: #d9d9d9;
    --cell: #ffffff;
    --cell-edge: #e2e2e2;
    --header: #72aacb;
    --header-text: #ffffff;
    --row-text: #6e4219;
    --ink: #1e1e1e;
    --from-text: #444444;
    --brand: #b3243a;
    --brand-mark: #1f4f84;
    --grass: #7cba3f;
    --cloud: #7fb5d5;
    --hill-top: #1a8422;
    --hill-bottom: #38a836;
    --wood: #c48a52;
    --wood-text: #5a3311;
  }
  * { box-sizing: border-box; }
  html, body {
    margin: 0;
    width: 1200px;
    height: 1073px;
    overflow: hidden;
  }
  body {
    position: relative;
    background: var(--sky);
    font-family: "Questrial", "Century Gothic", sans-serif;
  }

  .sky-glow {
    position: absolute;
    left: 500px; top: 0;
    width: 240px; height: 180px;
    background: radial-gradient(ellipse at center, var(--sky-glow) 0%, rgba(255,255,255,0) 65%);
  }

  .cloud-area {
    position: absolute;
    background: var(--cloud);
    border-radius: 40px;
  }
  .cloud-area--left { left: 50px; top: 273px; width: 216px; height: 126px; }
  .cloud-area--right { left: 920px; top: 568px; width: 125px; height: 130px; }

  .brand {
    position: absolute;
    left: 504px; top: 88px;
    display: flex;
    align-items: center;
    gap: 12px;
  }
  .brand__from { font-size: 22px; color: var(--from-text); }
  .brand__name {
    display: flex; align-items: center; gap: 8px;
    font-size: 22px; color: var(--brand);
  }
  .brand__mark {
    width: 14px; height: 14px;
    background: var(--brand-mark);
    border-radius: 50%;
  }

  .grass-area {
    position: absolute;
    left: 242px; top: 136px;
    width: 714px; height: 34px;
    background: var(--grass);
  }

  .panel {
    position: absolute;
    left: 266px; top: 167px;
    width: 669px; height: 680px;
    background: var(--panel);
    border: 1px solid var(--panel-edge);
    border-radius: 10px;
    box-shadow: 0 4px 8px rgba(0,0,0,0.25);
  }
  .panel__intro {
    position: absolute;
    left: 27px; top: 12px;
    margin: 0;
    font-size: 20px;
    font-weight: normal;
    color: var(--ink);
    white-space: nowrap;
  }
  .standings {
    position: absolute;
    left: 22px; top: 50px;
    border-collapse: separate;
    border-spacing: 7px 4.3px;
  }
  .standings th {
    height: 34px;
    background: var(--header);
    color: var(--header-text);
    font-family: "Open Sans", "Arial Narrow", sans-serif;
    font-weight: 800;
    font-size: 14px;
    letter-spacing: -0.2px;
    text-align: center;
    padding: 0;
    text-shadow: 0 1px 1px rgba(0,0,0,0.25);
  }
  .standings td {
    height: 35.5px;
    background: var(--cell);
    border: 1px solid var(--cell-edge);
    box-shadow: 0 1px 2px rgba(0,0,0,0.08);
    color: var(--row-text);
    font-size: 16px;
    padding: 0;
  }
  .standings .col-position { width: 134px; text-align: center; font-family: "Open Sans", sans-serif; font-weight: 700; font-size: 15px; }
  .standings .col-name { width: 322px; padding-left: 64px; text-align: left; }
  .standings th.col-name { padding-left: 0; text-align: center; }
  .standings .col-points { width: 134px; padding-left: 16px; text-align: left; }
  .standings th.col-points { padding-left: 0; text-align: center; }

  .hills-area {
    position: absolute;
    left: 0; top: 953px;
    width: 1200px; height: 120px;
    background: linear-gradient(180deg, var(--hill-top) 0%, var(--hill-bottom) 100%);
  }

  .signpost {
    position: absolute;
    left: 636px; top: 877px;
    width: 298px; height: 98px;
  }
  .signpost__area {
    position: absolute;
    inset: 0;
    background: var(--wood);
    border-radius: 4px;
  }
  .signpost__text {
    position: absolute;
    inset: 0;
    margin: 0;
    display: flex; align-items: center; justify-content: center;
    text-align: center;
    font-family: "Open Sans", sans-serif;
    font-weight: 700;
    font-size: 14px;
    line-height: 1.55;
    color: var(--wood-text);
    padding: 0 14px;
  }
</style>
</head>
<body>
  <div class="sky-glow"></div>

  <div class="cloud-area cloud-area--left" role="img" aria-label="Illustrated clouds in the sky"></div>
  <div class="cloud-area cloud-area--right" role="img" aria-label="Illustrated clouds in the sky"></div>

  <div class="brand">
    <span class="brand__from">From</span>
    <span class="brand__name"><span class="brand__mark"></span>brightloom goalpost</span>
  </div>

  <div class="grass-area" role="img" aria-label="Illustrated strip of grass along the top of the league panel"></div>

  <main class="panel">
    <h1 class="panel__intro">See how you are doing! Are your friends doing better or worse?</h1>
    <table class="standings">
      <thead>
        <tr><th class="col-position">POSITION</th><th class="col-name">NAME</th><th class="col-points">POINTS</th></tr>
      </thead>
      <tbody>
        <tr><td class="col-position">1</td><td class="col-name">Mara Ellwood</td><td class="col-points">3519</td></tr>
        <tr><td class="col-position">2</td><td class="col-name">Felix Arden</td><td class="col-points">2408</td></tr>
        <tr><td class="col-position">3</td><td class="col-name">Owen Pellick</td><td class="col-points">1956</td></tr>
        <tr><td class="col-position">4</td><td class="col-name">Ruth Calloway</td><td class="col-points">1813</td></tr>
        <tr><td class="col-position">5</td><td class="col-name">Hugo Brantwell</td><td class="col-points">486</td></tr>
        <tr><td class="col-position">6</td><td class="col-name">Nils Ostberg</td><td class="col-points">153</td></tr>
        <tr><td class="col-position">7</td><td class="col-name">Sam Whitlow</td><td class="col-points">-130</td></tr>
        <tr><td class="col-position">8</td><td class="col-name">Ravi Kestrel</td><td class="col-points">-323</td></tr>
        <tr><td class="col-position">9</td><td class="col-name">Tunde Ajalo</td><td class="col-points">-577</td></tr>
        <tr><td class="col-position">10</td><td class="col-name">Glen Harrow</td><td class="col-points">-1672</td></tr>
        <tr><td class="col-position">11</td><td class="col-name">Mara Ellwood</td><td class="col-points">-1900</td></tr>
        <tr><td class="col-position">12</td><td class="col-name">Felix Arden</td><td class="col-points">-2315</td></tr>
        <tr><td class="col-position">13</td><td class="col-name">Owen Pellick</td><td class="col-points">-2759</td></tr>
        <tr><td class="col-position">14</td><td class="col-name">Ruth Calloway</td><td class="col-points">-3001</td></tr>
      </tbody>
    </table>
  </main>

  <div class="hills-area" role="img" aria-label="Illustrated rolling green hills"></div>

  <div class="signpost">
    <div class="signpost__area" role="img" aria-label="Illustrated wooden signpost carrying the next game announcement"></div>
    <p class="signpost__text">Don't forget to play GRAND CUP<br>QUAL 2 !</p>
  </div>
</body>
</html>
```